Halvessa Orbital needs a standing banner

Halvessa Orbital banner
We need a standing banner for Halvessa Orbital (www.halvessaorbital.com.au).
The banner should be: 1000mm (wide) x 2200mm (high) and high resolution.
All images should be either those supplied with these specifications or Public Domain (CC0).
Templates for the banner attached (Refer StandardPullUp_Templates_1000x2200.pdf file)
About us:
We provide high quality professional services for the Australian space industry, such as consultation, contracted personnel, and project delivery. Our clients include organisations working in the space industry. We work with companies that produce communications systems, satellites, launchpad technology, space situational awareness, and Internet-of-Things (IoT) technology being developed within the space industry.
The banner will promote Halvessa Orbital to potential space customers at events, trade shows, and presentations, and should be professional, visually appealing, clear, and uncluttered.
Logo:
Include the Halvessa Orbital logo or the Halvessa Orbital heading (both are attached).
Text:
The banner should include some text but not be too cluttered. Include some of the following text:
[Choose from the following:]
Delivering value to our clients in a manner that inspires.
Delivering excellence in Space Professional Services
Specialised Support Service Provider
Bringing exceptional talent to the Australian space sector.
[And select a sentence or two from the following:]
Our services aim to fast-track project development, pre-empt and solve problems more efficiently, and inspire and guide success.
We understand cybersecurity technologies, communications, systems engineering, systems design, facilities, integration, infrastructure, and modern systems development principles.
By leveraging our skills and experience, we understand your problems and can identify talented people both locally and internationally that deliver the solutions you need.
Halvessa staff have been in the forefront of major program deliveries to defence and commercial clients across the maritime and defence market for decades.
Our staff are leaders in their field and pioneers in the establishment of systematic approaches to the most complex problems.
---
You can also see our website (www.halvessaorbital.com.au) for more text to choose from
However, don’t overload the banner with text – keep it to the logo, a branding statement, and a sentence or two at the most. A captivating design with imagery is what we are after.
Images:
Images should be recent, high resolution, Australian (where possible), and realistic. Images with people in a technology or Space related industry setting are good. Suggestions include professionals working in mission control stations or technical/office environments. Other images might include mission control centres, rockets, satellites, radio communications equipment, large satellite dishes, night landscapes with stars, or pictures of Australia or Earth from space. Include both graphics and photos.
NO cartoons or space shuttles from the 1980s please.
Images should be current rather than old. See our website for some example images, though you are encouraged to use images other than these.
Colours:
We would like the colours to match the Halvessa Orbital logo, using mainly: navy blue (#000080) and matching blues; platinum (#E5E4E2), rocket metallic (#8A7F8D) and similar greys; black (#000000), and white (#FFFFFF). Sunlight colours may be included sparingly as a highlight.
Attached files:
- I have attached the Halvessa Orbital logo which must appear on the banner (‘halvessaorbital.ai’)
- I have attached the Halvessa Orbital heading, which may also appear on the banner (‘halvessaorbital-heading.psd’)
We look forward to seeing your designs!

```html
<!DOCTYPE html>
<html lang="en">
<head>
<meta charset="utf-8">
<title>Halvessa Orbital – Standing Banner</title>
<link rel="stylesheet" href="https://fonts.googleapis.com/css2?family=Bebas+Neue&family=Source+Sans+3:wght@400;600;700;800&display=swap">
<style>
  :root {
    --canvas-bg: #f4e6da;
    --navy: #272a7b;
    --metallic: #8a7f8d;
    --platinum: #e5e4e2;
    --ring-blue: #a9d1f1;
    --white: #ffffff;
    --text-grey: #5a5a5e;
    --list-grey: #55555a;
    --url-grey: #46464b;
    --shadow-black: #000000;
  }
  * { margin: 0; padding: 0; box-sizing: border-box; }
  html, body {
    width: 1147px;
    height: 1200px;
    overflow: hidden;
    background: var(--canvas-bg);
  }
  .banner {
    position: absolute;
    left: 313px;
    top: 28px;
    width: 520px;
    height: 1144px;
    background: var(--white);
    overflow: hidden;
    font-family: "Source Sans 3", sans-serif;
  }
  .banner-shapes {
    position: absolute;
    inset: 0;
    width: 520px;
    height: 1144px;
  }
  .brand-name {
    position: absolute;
    left: 18px;
    top: 62px;
    width: 190px;
    text-align: center;
    font-weight: 700;
    font-size: 27px;
    line-height: 1.05;
    color: var(--navy);
    letter-spacing: 0.4px;
  }
  .headline {
    position: absolute;
    left: 38px;
    top: 290px;
    font-family: "Bebas Neue", sans-serif;
    font-weight: 400;
    font-size: 60px;
    line-height: 59px;
    color: var(--white);
    text-shadow: 3px 3px 0 var(--shadow-black);
  }
  .photo-circle {
    position: absolute;
    border-radius: 50%;
    border: 6px solid var(--ring-blue);
    box-shadow: 0 0 0 2px var(--white);
  }
  .photo-capsule {
    left: 27px; top: 560px; width: 140px; height: 140px;
    background: radial-gradient(circle at 45% 50%, #dfe3ea 0%, #8f99a8 28%, #1b2230 55%, #05070c 100%);
  }
  .photo-dishes {
    left: 158px; top: 550px; width: 152px; height: 152px;
    background: radial-gradient(circle at 60% 70%, #e6e6e2 0%, #9a8f6e 25%, #6f7046 55%, #4d5a35 100%);
  }
  .photo-control {
    left: 289px; top: 476px; width: 206px; height: 206px;
    background: radial-gradient(circle at 55% 60%, #2b3b55 0%, #41618a 40%, #7fa6cf 75%, #b9cfe6 100%);
  }
  .intro {
    position: absolute;
    left: 47px;
    top: 742px;
    width: 208px;
    font-weight: 400;
    font-size: 17px;
    line-height: 21.5px;
    color: var(--text-grey);
  }
  .intro p + p { margin-top: 10px; }
  .service-list {
    position: absolute;
    left: 280px;
    top: 746px;
    width: 190px;
    list-style: none;
  }
  .service-list li {
    position: relative;
    padding-left: 28px;
    margin-bottom: 10px;
    font-weight: 800;
    font-size: 15px;
    line-height: 18.5px;
    color: var(--list-grey);
    text-transform: uppercase;
  }
  .service-list li svg {
    position: absolute;
    left: 0;
    top: 0;
    width: 17px;
    height: 17px;
  }
  .web-pill {
    position: absolute;
    left: 104px;
    top: 1058px;
    width: 292px;
    height: 44px;
    border-radius: 22px;
    background: var(--white);
    border: 3px solid var(--navy);
    text-align: center;
    font-weight: 700;
    font-size: 19px;
    line-height: 38px;
    color: var(--url-grey);
    letter-spacing: 0.2px;
  }
</style>
</head>
<body>
  <section class="banner" aria-label="Halvessa Orbital standing banner">
    <svg class="banner-shapes" viewBox="0 0 520 1144">
      <defs>
        <linearGradient id="spaceGradient" x1="0" y1="0" x2="0.3" y2="1">
          <stop offset="0" stop-color="#0d1e3c"/>
          <stop offset="0.32" stop-color="#2d5f92"/>
          <stop offset="0.55" stop-color="#5d8cbd"/>
          <stop offset="0.75" stop-color="#1f4f7c"/>
          <stop offset="1" stop-color="#0b2a4a"/>
        </linearGradient>
      </defs>
      <path role="img" aria-label="Astronaut floating in space above the Earth"
            d="M0 0 H520 V470 C400 520 220 590 0 604 Z" fill="url(#spaceGradient)"/>
      <path d="M0 604 C220 590 400 520 520 470 V478 C400 540 220 610 0 622 Z" fill="var(--metallic)"/>
      <path d="M0 622 C220 610 400 540 520 478 V505 C420 580 240 660 0 680 Z" fill="var(--navy)"/>
      <path d="M470 470 L520 440 V470 Z" fill="var(--navy)"/>
      <circle cx="86" cy="46" r="150" fill="var(--navy)"/>
      <circle cx="80" cy="38" r="150" fill="var(--white)"/>
      <path d="M0 992 Q260 1070 520 1004 V1144 H0 Z" fill="var(--metallic)"/>
      <path d="M0 1004 Q260 1082 520 1016 V1144 H0 Z" fill="var(--navy)"/>
    </svg>

    <div class="brand-name">Halvessa<br>Orbital</div>

    <h1 class="headline">Delivering<br>Excellence in<br>Space Professional<br>Services</h1>

    <div class="photo-circle photo-capsule" role="img" aria-label="Crew capsule spacecraft in orbit"></div>
    <div class="photo-circle photo-dishes" role="img" aria-label="Aerial view of a ground station with large satellite dishes"></div>
    <div class="photo-circle photo-control" role="img" aria-label="Professionals working at consoles in a mission control centre"></div>

    <div class="intro">
      <p>Our services aim to fast-track project development, pre-empt and solve problems more efficiently to inspire and guide success.</p>
      <p>Halvessa staff have been in the forefront of major program deliveries to defence and commercial clients across the maritime and defence market for decades.</p>
    </div>

    <ul class="service-list">
      <li><svg viewBox="0 0 18 18"><circle cx="9" cy="9" r="7.5" fill="none" stroke="#272a7b" stroke-width="2"/><path d="M5.5 9.2 L8 11.6 L12.6 6.6" fill="none" stroke="#272a7b" stroke-width="2" stroke-linecap="round" stroke-linejoin="round"/></svg>Cyber Security Technologies</li>
      <li><svg viewBox="0 0 18 18"><circle cx="9" cy="9" r="7.5" fill="none" stroke="#272a7b" stroke-width="2"/><path d="M5.5 9.2 L8 11.6 L12.6 6.6" fill="none" stroke="#272a7b" stroke-width="2" stroke-linecap="round" stroke-linejoin="round"/></svg>Communications</li>
      <li><svg viewBox="0 0 18 18"><circle cx="9" cy="9" r="7.5" fill="none" stroke="#272a7b" stroke-width="2"/><path d="M5.5 9.2 L8 11.6 L12.6 6.6" fill="none" stroke="#272a7b" stroke-width="2" stroke-linecap="round" stroke-linejoin="round"/></svg>Systems<br>Engineering</li>
      <li><svg viewBox="0 0 18 18"><circle cx="9" cy="9" r="7.5" fill="none" stroke="#272a7b" stroke-width="2"/><path d="M5.5 9.2 L8 11.6 L12.6 6.6" fill="none" stroke="#272a7b" stroke-width="2" stroke-linecap="round" stroke-linejoin="round"/></svg>Systems Design</li>
      <li><svg viewBox="0 0 18 18"><circle cx="9" cy="9" r="7.5" fill="none" stroke="#272a7b" stroke-width="2"/><path d="M5.5 9.2 L8 11.6 L12.6 6.6" fill="none" stroke="#272a7b" stroke-width="2" stroke-linecap="round" stroke-linejoin="round"/></svg>Facilities</li>
      <li><svg viewBox="0 0 18 18"><circle cx="9" cy="9" r="7.5" fill="none" stroke="#272a7b" stroke-width="2"/><path d="M5.5 9.2 L8 11.6 L12.6 6.6" fill="none" stroke="#272a7b" stroke-width="2" stroke-linecap="round" stroke-linejoin="round"/></svg>Integration</li>
      <li><svg viewBox="0 0 18 18"><circle cx="9" cy="9" r="7.5" fill="none" stroke="#272a7b" stroke-width="2"/><path d="M5.5 9.2 L8 11.6 L12.6 6.6" fill="none" stroke="#272a7b" stroke-width="2" stroke-linecap="round" stroke-linejoin="round"/></svg>Infrastructure</li>
      <li><svg viewBox="0 0 18 18"><circle cx="9" cy="9" r="7.5" fill="none" stroke="#272a7b" stroke-width="2"/><path d="M5.5 9.2 L8 11.6 L12.6 6.6" fill="none" stroke="#272a7b" stroke-width="2" stroke-linecap="round" stroke-linejoin="round"/></svg>Modern Systems Development</li>
    </ul>

    <div class="web-pill">www.halvessaorbital.com.au</div>
  </section>
</body>
</html>
```